Stainless Steel Business Card

I have a fiber laser and want to highlight its capabilities in a business card. On the card I want

Brevik Industries
Martin Brevik
martin@mbrevik-mail.net
417-555-0163

This will be cut / engraved on stainless steel. I want the Brevik Industries to be prominent with laser cut font so that there are no dropouts on the O and A's. My name email and phone number should be engraved black. I would like some cool geometric patterns to cutout on the card to highlight the capabilities of my machine. I will need to files in the end either SVG or dxf of the engrave portion and the cut portion.

```html
<!DOCTYPE html>
<html lang="en">
<head>
<meta charset="utf-8">
<title>Brevik Industries – Business Card</title>
<link rel="stylesheet" href="https://fonts.googleapis.com/css2?family=Arimo:wght@700&family=Saira+Stencil+One&family=Allerta+Stencil&display=swap">
<style>
  :root {
    --page: #ffffff;
    --card: #ffffff;
    --ink: #000000;
    --cutout-dark: #4a4a4a;
    --cutout-light: #7a7a7a;
  }
  html, body {
    margin: 0;
    padding: 0;
    width: 1200px;
    height: 959px;
    overflow: hidden;
    background: var(--page);
  }
  .canvas {
    display: block;
    width: 1200px;
    height: 959px;
  }
  .card-outline {
    fill: var(--card);
    stroke: var(--ink);
    stroke-width: 1;
  }
  .brand-name {
    font-family: "Saira Stencil One", "Allerta Stencil", Impact, sans-serif;
    font-size: 200px;
    fill: var(--ink);
  }
  .brand-tagline {
    font-family: "Allerta Stencil", "Saira Stencil One", Arial, sans-serif;
    font-size: 92px;
    fill: var(--ink);
  }
  .contact {
    font-family: "Arimo", Arial, sans-serif;
    font-weight: 700;
    fill: var(--ink);
  }
  .person-name { font-size: 41px; }
  .email { font-size: 28px; }
  .phone { font-size: 39px; }
  .icon { fill: var(--ink); }
  .icon-line { fill: none; stroke: var(--card); stroke-width: 2; }
</style>
</head>
<body>
<svg class="canvas" viewBox="0 0 1200 959" xmlns="http://www.w3.org/2000/svg">
  <defs>
    <linearGradient id="cutoutTone" x1="0" y1="0" x2="1" y2="1">
      <stop offset="0" stop-color="var(--cutout-dark)"/>
      <stop offset="1" stop-color="var(--cutout-light)"/>
    </linearGradient>
  </defs>

  <rect class="card-outline" x="180" y="227" width="871" height="524" rx="50" ry="50"/>

  <polygon class="cut-pattern" role="img"
           aria-label="Geometric circuit-trace cutout pattern of diagonal lines and chevrons in the lower left corner of the card"
           points="211,389 293,473 415,477 388,565 583,565 524,624 617,716 276,716 211,684"
           fill="url(#cutoutTone)"/>

  <text class="brand-name" x="259" y="428" textLength="754" lengthAdjust="spacingAndGlyphs">BREVIK</text>
  <text class="brand-tagline" x="1016" y="510" text-anchor="end">Industries</text>

  <text class="contact person-name" x="1010" y="627" text-anchor="end">Martin Brevik</text>

  <g class="icon-mail" transform="translate(611 648)">
    <rect class="icon" x="0" y="0" width="40" height="27"/>
    <polyline class="icon-line" points="1,1 20,15 39,1"/>
    <line class="icon-line" x1="1" y1="26" x2="15" y2="12"/>
    <line class="icon-line" x1="39" y1="26" x2="25" y2="12"/>
  </g>
  <text class="contact email" x="1011" y="668" text-anchor="end">martin@mbrevik-mail.net</text>

  <g class="icon-phone" transform="translate(722 681) scale(1.5)">
    <path class="icon" d="M6.6 10.8c1.4 2.8 3.8 5.1 6.6 6.6l2.2-2.2c.3-.3.7-.4 1-.2 1.1.4 2.3.6 3.6.6.6 0 1 .4 1 1V20c0 .6-.4 1-1 1C10.6 21 3 13.4 3 4c0-.6.4-1 1-1h3.5c.6 0 1 .4 1 1 0 1.3.2 2.5.6 3.6.1.3 0 .7-.2 1z"/>
  </g>
  <text class="contact phone" x="1014" y="709" text-anchor="end">417-555-0163</text>
</svg>
</body>
</html>
```